Scoopa Verde label for 16oz jar

We need a design for a label for a 16oz glass jar for salsa (dimensions in inches- 2.75 x9.5). Name of salsa is “Scoopa Verde” and needs to include a place for medium or hot for the different flavors. Looking for bright Fiesta colors but a mature look. Attached is an image of the coloring scheme we like. There will need to be nutrition facts on one end and a description of the product/flavor on the other side of the label. Ultimately at this point looking for brand design.

```html
<!DOCTYPE html>
<html lang="en">
<head>
<meta charset="utf-8">
<title>Scoopa Verde Hot Salsa Label</title>
<link href="https://fonts.googleapis.com/css2?family=Bangers&family=Roboto+Condensed:wght@400;700&display=swap" rel="stylesheet">
<style>
:root{
  --ink:#000;
  --paper:#fff;
  --fiesta-yellow:#f7b82b;
  --fiesta-orange:#f5a21f;
  --fiesta-red:#e3252b;
  --deep-red:#b81d22;
  --logo-pink:#ec1a6b;
  --salsa-yellow:#f9c51b;
}
*{margin:0;padding:0;box-sizing:border-box}
html,body{width:1200px;height:347px;overflow:hidden;background:var(--ink)}
.label{position:relative;width:1200px;height:347px;background:var(--ink);font-family:"Roboto Condensed",sans-serif;color:var(--paper)}
.fiesta-band{position:absolute;left:0;width:1200px;height:48px;background:linear-gradient(180deg,var(--fiesta-orange) 0%,var(--fiesta-red) 55%,var(--fiesta-orange) 80%,var(--fiesta-red) 100%)}
.fiesta-band.top{top:12px}
.fiesta-band.bottom{top:287px;background:linear-gradient(180deg,var(--fiesta-red) 0%,var(--fiesta-orange) 20%,var(--fiesta-red) 45%,var(--fiesta-orange) 100%)}
.art{position:absolute;border-radius:3px}
.art.hat-area{left:600px;top:10px;width:262px;height:92px;background:linear-gradient(180deg,var(--fiesta-orange),var(--fiesta-red))}
.art.cactus-area{left:432px;top:80px;width:50px;height:203px;background:var(--fiesta-red)}
.art.pepper-area{left:500px;top:218px;width:130px;height:64px;background:linear-gradient(180deg,var(--fiesta-red),var(--deep-red))}
.tagline{position:absolute;left:71px;top:94px;font-family:"Bangers",sans-serif;color:var(--fiesta-yellow)}
.tagline h1{font-size:27px;font-weight:400;letter-spacing:1.2px;line-height:1}
.tagline p{margin-top:8px;font-size:13px;line-height:10.6px;letter-spacing:.7px}
.care{position:absolute;left:71px;top:197px;font-size:15.5px;font-weight:700}
.maker{position:absolute;left:245px;top:230px;font-size:14px;line-height:15.5px;font-weight:700}
.brand-name{position:absolute;left:470px;top:92px;width:340px;text-align:center;font-family:"Bangers",sans-serif;font-size:124px;line-height:1;color:var(--logo-pink);letter-spacing:0}
.product-type{position:absolute;left:651px;top:228px;font-family:"Bangers",sans-serif;font-size:56px;line-height:1;color:var(--salsa-yellow);letter-spacing:2px}
.heat{position:absolute;left:826px;top:208px;transform:rotate(-90deg);transform-origin:top left;font-size:26px;font-weight:700;color:var(--fiesta-red);letter-spacing:7px;line-height:1}
.net-wt{position:absolute;left:828px;top:248px;font-size:15.5px;line-height:17px;font-weight:700}
.nutrition{position:absolute;left:947px;top:26px;width:162px;height:304px;background:var(--paper);color:var(--ink);border:2px solid var(--ink);outline:2px solid var(--paper);padding:3px 5px;font-size:8px;line-height:1}
.nutrition h2{font-size:20px;font-weight:700;line-height:1;border-bottom:1px solid var(--ink);padding-bottom:2px}
.nf-servings{font-size:7.5px;margin-top:2px}
.nf-size{display:flex;justify-content:space-between;font-size:12px;font-weight:700;border-bottom:5px solid var(--ink);padding-bottom:2px}
.nf-amount{font-size:6.5px;font-weight:700;margin-top:2px}
.nf-calories{display:flex;justify-content:space-between;align-items:flex-end;font-size:16px;font-weight:700;border-bottom:3px solid var(--ink);padding-bottom:1px}
.nf-calories span:last-child{font-size:22px}
.nf-dv{text-align:right;font-size:7.5px;font-weight:700;padding:2px 0;border-bottom:1px solid var(--ink)}
.nf-row{display:flex;justify-content:space-between;height:12.2px;align-items:center;border-bottom:1px solid var(--ink)}
.nf-row.indent{padding-left:5px}
.nf-row.thick{border-bottom:4px solid var(--ink);height:14px}
.nf-row b{font-weight:700}
.nf-row.last{border-bottom:3px solid var(--ink)}
.nf-note{font-size:5.6px;line-height:1.2;margin-top:2px}
.ingredients{position:absolute;left:1119px;top:278px;width:197px;transform:rotate(-90deg);transform-origin:top left;font-size:6.6px;line-height:10.5px;text-transform:uppercase}
</style>
</head>
<body>
<div class="label">
  <div class="fiesta-band top" role="img" aria-label="Fiesta zigzag border band in orange and red"></div>
  <div class="fiesta-band bottom" role="img" aria-label="Fiesta zigzag border band in orange and red"></div>

  <div class="tagline">
    <h1>A Recipe for Double Dippin'!</h1>
    <p>Our hot salsa has the same southwest blend<br>of zesty with the spice level kicked into high gear.<br>Scoopa cautiously!</p>
  </div>
  <p class="care">Refrigerate after opening. Best served chilled.</p>
  <p class="maker">Manufactured for:<br>Scoopa Verde Foods, LLC<br>Harlow, KS 66099</p>

  <div class="art cactus-area" role="img" aria-label="Red cactus illustration"></div>
  <div class="art hat-area" role="img" aria-label="Colourful sombrero illustration"></div>
  <div class="art pepper-area" role="img" aria-label="Red chili peppers illustration"></div>

  <div class="brand-name">Scoopa</div>
  <div class="product-type">SALSA</div>
  <div class="heat">HOT</div>
  <p class="net-wt">NET WT.<br>16OZ (453G)</p>

  <section class="nutrition">
    <h2>Nutrition Facts</h2>
    <p class="nf-servings">16 servings per container</p>
    <div class="nf-size"><span>Serving Size</span><span>2 Tbsp (28g)</span></div>
    <p class="nf-amount">Amount Per Serving</p>
    <div class="nf-calories"><span>Calories</span><span>10</span></div>
    <p class="nf-dv">% Daily Value*</p>
    <div class="nf-row"><span><b>Total Fat</b> 0g</span><b>0%</b></div>
    <div class="nf-row indent"><span>Saturated Fat 0g</span><b>0%</b></div>
    <div class="nf-row indent"><span>Trans Fat 0g</span><span></span></div>
    <div class="nf-row"><span><b>Cholesterol</b> 0 mg</span><b>0%</b></div>
    <div class="nf-row"><span><b>Sodium</b> 210mg</span><b>9%</b></div>
    <div class="nf-row"><span><b>Total Carbohydrate</b> 2g</span><b>1%</b></div>
    <div class="nf-row indent"><span>Dietary Fiber 0g</span><b>0%</b></div>
    <div class="nf-row indent"><span>Total Sugar &lt;1 g</span><span></span></div>
    <div class="nf-row indent"><span>Includs 0g Added Sugars</span><b>0%</b></div>
    <div class="nf-row thick"><span><b>Protein</b> 0g</span><span></span></div>
    <div class="nf-row"><span>Vitamin D 0mcg</span><b>0%</b></div>
    <div class="nf-row"><span>Calcium 20mg</span><b>2%</b></div>
    <div class="nf-row"><span>Iron 0,4mg</span><b>2%</b></div>
    <div class="nf-row last"><span>Potassium 10mg</span><b>0%</b></div>
    <p class="nf-note">* The % Daily Value (DV) tells you how much a nutrient in a serving of food contributes to a daily diet. 2,000 calories a day is used for general nutrition advice.</p>
  </section>

  <p class="ingredients">Ingredients: diced tomatoes (tomatoes, tomato juice, &lt;2% of: salt, citric acid, calcium chloride), cilantro, jalapeno peppers, cumin, kosher salt, granulated garlic, the juice of fresh limes, dehydrated onion, black pepper, celery salt.</p>
</div>
</body>
</html>
```